The Copperwell

We need a APP for our members. this is a Private Bar/Venue. history of the brick building is it was built in1898 and was a gentleman club, oyster house, cigar factory and then law offices before we purchased and are beginning restoration.
the APP must include
1. direct texting to the concierge
2. calendar of events
3. vantor Lock To open the lock, anyone with a code can approach the door, enable their phone's Bluetooth and press the relevant address from the app.
Read more: http://www.evenpostgazette.co.uk/sciencetech/article-4418206/farewell-metal-keys-phone-bolt-opens-front-door-without-anything-in-hand.html#ixzz9kQR2mpaL
4. Menus from various restaurants from our surrounding area
5. member name and member number to give the feel that the app is personalized
6. the members account balance
7. ability to pay their bill with credit card or quid line monthly and automatically.
8. link to züro with its own icon within the app.
9.the ability to reserve the room
Anything else that may of interest for our members that may be relevant that I may not have mentioned since we are new at this...
35 to 60 years of age
Club

```html
<!DOCTYPE html>
<html lang="en">
<head>
<meta charset="utf-8">
<title>The Copperwell – Reserve the Room</title>
<link rel="stylesheet" href="https://fonts.googleapis.com/css2?family=Open+Sans:wght@400&display=swap">
<style>
  :root {
    --header-bg: #4b4d4d;
    --header-ink: #ffffff;
    --page-bg: #ffffff;
    --label-ink: #939699;
    --field-border: #9a9c9e;
    --button-bg: #979a9c;
    --button-ink: #ffffff;
  }
  * { box-sizing: border-box; margin: 0; padding: 0; }
  html, body {
    width: 675px;
    height: 1200px;
    overflow: hidden;
    background: var(--page-bg);
    font-family: "Open Sans", sans-serif;
  }
  .screen {
    position: relative;
    width: 675px;
    height: 1200px;
    background: var(--page-bg);
  }
  .app-bar {
    position: absolute;
    left: 0; top: 0;
    width: 675px;
    height: 126px;
    background: var(--header-bg);
  }
  .menu-icon {
    position: absolute;
    left: 37px;
    top: 44px;
  }
  .app-title {
    position: absolute;
    left: 0; right: 0;
    top: 30px;
    text-align: center;
    color: var(--header-ink);
    font-size: 53px;
    font-weight: 400;
    line-height: 64px;
    letter-spacing: 0.5px;
  }
  .field-label {
    position: absolute;
    left: 50px;
    color: var(--label-ink);
    font-size: 32px;
    line-height: 40px;
    font-weight: 400;
  }
  .field-box {
    position: absolute;
    left: 50px;
    height: 42px;
    border: 2px solid var(--field-border);
    border-radius: 7px;
    background: var(--page-bg);
  }
  .field-box--wide { width: 575px; }
  .field-box--short { width: 120px; }
  .date-part {
    position: absolute;
    width: 120px;
  }
  .date-part .field-box {
    position: static;
    display: block;
    width: 120px;
  }
  .date-hint {
    display: block;
    text-align: center;
    color: var(--label-ink);
    font-size: 14px;
    line-height: 20px;
    margin-top: 2px;
  }
  .reserve-button {
    position: absolute;
    left: 52px;
    top: 1004px;
    width: 577px;
    height: 130px;
    background: var(--button-bg);
    color: var(--button-ink);
    border: none;
    border-radius: 2px;
    font-family: "Open Sans", sans-serif;
    font-size: 33px;
    line-height: 130px;
    text-align: center;
  }
</style>
</head>
<body>
<main class="screen">
  <header class="app-bar">
    <svg class="menu-icon" width="51" height="40" viewBox="0 0 51 40" aria-hidden="true">
      <rect x="0" y="0.5" width="51" height="3" fill="var(--header-ink)"/>
      <rect x="0" y="18.5" width="51" height="3" fill="var(--header-ink)"/>
      <rect x="0" y="35.5" width="51" height="3" fill="var(--header-ink)"/>
    </svg>
    <h1 class="app-title">ROOM</h1>
  </header>

  <form class="reservation-form">
    <label class="field-label" style="top:180px">Name:</label>
    <div class="field-box field-box--wide" style="top:236px"></div>

    <label class="field-label" style="top:299px">Surname:</label>
    <div class="field-box field-box--wide" style="top:355px"></div>

    <label class="field-label" style="top:419px">From:</label>
    <div class="date-part" style="left:50px; top:474px"><span class="field-box"></span><span class="date-hint">dd</span></div>
    <div class="date-part" style="left:188px; top:474px"><span class="field-box"></span><span class="date-hint">mm</span></div>
    <div class="date-part" style="left:327px; top:474px"><span class="field-box"></span><span class="date-hint">yy</span></div>

    <label class="field-label" style="top:559px">To:</label>
    <div class="date-part" style="left:50px; top:614px"><span class="field-box"></span><span class="date-hint">dd</span></div>
    <div class="date-part" style="left:188px; top:614px"><span class="field-box"></span><span class="date-hint">mm</span></div>
    <div class="date-part" style="left:327px; top:614px"><span class="field-box"></span><span class="date-hint">yy</span></div>

    <label class="field-label" style="top:699px">Email:</label>
    <div class="field-box field-box--wide" style="top:754px"></div>

    <label class="field-label" style="top:818px">People:</label>
    <div class="field-box field-box--short" style="top:873px"></div>

    <button class="reserve-button" type="button">Reserve the Room</button>
  </form>
</main>
</body>
</html>
```